Website Design for Harbor 7340

We need a website design for a new company that strives to provide training and structure for religious missionaries who are traveling the world to teach of christianity.
They provide training in:
- Nutrition Coaching & Daily assignments
- Personal Training Sessions
- Phycological emotional/mental component
The goal of Harbor 7340 is to help missionaries preach the gospel of christ to those who haven't heard it due to geographical obstacles and physical limitations that get in the way.
The homepage template has linked images to use. If any other images are needed, stock images are acceptable.

Logo/Color Scheme: https://files.quorvex.net/share/8Kd2Lm9XpQ4rTz7WvN3bYc6HsJ1aFe0Gu

Customer Avatar/Core Message Canvas: https://sheets.plendora.net/s/4Rq81ZtyMn2wXcVb7KpLd0HsJ9aFgE3QuTo6YiPxNe/view

Homepage Template: https://docs.plendora.net/d/7Nw52KxpTr8vYzQm3LcBf1GhJ6dSeA0RuWo4XiZqPk/view

```html
<!DOCTYPE html>
<html lang="en">
<head>
<meta charset="utf-8">
<title>Harbor 7340 — Missionary Training</title>
<link rel="stylesheet" href="https://fonts.googleapis.com/css2?family=Archivo+Black&family=Poppins:ital,wght@0,400;0,500;0,600;0,700;1,400&display=swap">
<style>
:root{
  --forest:#2b3318;
  --forest-soft:#323b1f;
  --gold:#e6bb47;
  --gold-pale:#f6e6b6;
  --ink:#2f2f2f;
  --muted:#555;
  --paper:#ffffff;
  --mist:#d7d7d7;
  --card:#f4f4f4;
}
*{margin:0;padding:0;box-sizing:border-box}
html,body{width:1200px;height:4270px;overflow:hidden}
body{position:relative;font-family:"Poppins",sans-serif;color:var(--ink);background:var(--paper)}
.abs{position:absolute}
.center{left:0;width:1200px;text-align:center}
a{color:inherit;text-decoration:none}

/* header */
.site-header{top:0;left:0;width:1200px;height:125px;background:var(--paper)}
.brand{left:86px;top:38px;display:flex;align-items:center;gap:10px;font-family:"Poppins",sans-serif;font-weight:700;font-size:34px;color:var(--forest);letter-spacing:1px}
.brand-square{width:22px;height:22px;background:var(--gold)}
.main-nav a{position:absolute;top:45px;font-size:15px;color:#444}
.signup{left:1003px;top:38px;width:110px;height:37px;background:var(--forest);color:#fff;font-size:14px;display:flex;align-items:center;justify-content:center;gap:8px}

/* hero */
.hero{top:125px;left:0;width:1200px;height:538px;background:linear-gradient(180deg,#5f6a6c 0%,#8c9596 30%,#6e7560 62%,#3d4628 100%)}
.hero-title{top:290px;font-family:"Archivo Black",sans-serif;font-size:44px;line-height:62px;color:#fff;text-shadow:0 3px 6px rgba(0,0,0,.6);letter-spacing:.5px}
.hero-sub{top:440px;font-size:15px;line-height:19px;color:#fff}
.btn{position:absolute;display:flex;align-items:center;justify-content:center;font-size:20px}
.btn-gold{background:var(--gold);color:#fff}
.btn-dark{background:var(--forest);color:#fff}
.dots{top:613px;left:563px;display:flex;gap:6px}
.dots span{width:14px;height:14px;background:#bfbfbf}
.dots span:first-child{background:#fff}

/* staff */
.section-title{font-size:42px;line-height:62px;font-weight:500;color:var(--forest)}
.staff-item{position:absolute;top:892px;width:150px;margin-left:-75px;text-align:center;font-size:17px;line-height:21px;color:#333}
.staff-badge{width:94px;height:94px;margin:0 auto 20px;background:var(--forest);clip-path:polygon(30% 0,70% 0,100% 30%,100% 70%,70% 100%,30% 100%,0 70%,0 30%);position:relative}
.staff-badge::after{content:"";position:absolute;left:32px;top:24px;width:30px;height:46px;border-radius:15px 15px 6px 6px;background:var(--gold)}

/* why */
.why{top:1137px;left:0;width:1200px;height:575px;background:var(--forest)}
.gold-title{font-size:42px;font-weight:600;color:var(--gold)}
.why-copy{top:1306px;left:205px;width:790px;text-align:center;font-size:15.5px;line-height:25px;color:#fff}
.why-quote{top:1437px;left:205px;width:790px;text-align:center;font-size:15.5px;line-height:25px;color:#fff;font-style:italic}
.why-ref{top:1524px;font-size:15px;color:var(--gold)}

/* approach */
.approach-sub{top:1822px;font-size:30px;font-weight:500;color:var(--gold)}
.pillar{position:absolute;top:1930px;width:325px;height:410px}
.pillar svg{position:absolute;left:0;top:0}
.pillar-name{position:absolute;top:45px;left:0;width:325px;text-align:center;font-size:27px;color:#fff;font-weight:500}
.pillar-text{position:absolute;top:132px;left:32px;width:261px;text-align:center;font-size:15.5px;line-height:25px;color:#555}

/* audience */
.audience{top:2535px;left:0;width:1200px;height:807px;background:var(--forest)}
.tab{position:absolute;left:103px;width:543px;height:85px;border:1px solid var(--gold);color:#fff;font-size:23px;font-weight:500;display:flex;align-items:center;padding-left:40px}
.tab.active{background:#fff;color:var(--forest);border-color:#fff}
.tab.active::after{content:"";position:absolute;right:-16px;top:33px;border-left:16px solid #fff;border-top:10px solid transparent;border-bottom:10px solid transparent}
.panel{top:2777px;left:669px;width:444px;height:325px;background:var(--forest-soft);padding:40px 60px}
.panel h3{font-size:21px;font-weight:400;color:var(--gold)}
.panel hr{border:0;height:2px;width:66px;background:var(--gold);margin:10px 0 14px}
.panel p{font-size:15.5px;line-height:25px;color:#fff;text-align:justify}

/* newsletter */
.newsletter{top:3342px;left:0;width:1200px;height:529px;background:var(--mist)}
.news-title{top:3424px;font-size:32px;line-height:42px;font-weight:600;color:var(--forest)}
.news-sub{top:3568px;font-size:15px;line-height:24px;color:#666}
.signup-form{top:3659px;left:187px;width:791px;height:96px;background:#fff}
.email{position:absolute;left:42px;top:34px;font-size:21px;color:#999}
.subscribe{left:514px;top:13px;width:263px;height:70px;background:var(--forest);color:var(--gold);font-size:22px;border-radius:4px}

/* footer */
.site-footer{top:3871px;left:0;width:1200px;height:298px;background:var(--forest)}
.footer-brand{left:103px;top:3972px;display:flex;align-items:center;gap:12px;font-weight:700;font-size:44px;color:#fff;letter-spacing:1px}
.footer-nav{top:4082px;left:103px;display:flex;font-size:16px;color:#fff}
.footer-nav a{padding:0 26px;border-left:1px solid #fff;line-height:34px}
.footer-nav a:first-child{padding-left:0;border-left:0}
.contact{position:absolute;left:855px;display:flex;gap:12px;color:#fff;font-size:15px;line-height:19px}
.contact .label{color:var(--gold);font-weight:600}
.bottom-bar{top:4169px;left:0;width:1200px;height:101px;background:var(--gold);color:#fff;font-size:15px}
.socials{position:absolute;left:900px;top:31px;display:flex;gap:13px}
.socials span{width:44px;height:44px;border:2px solid #fff;border-radius:50%}
</style>
</head>
<body>

<header class="site-header abs">
  <a class="brand abs" href="#"><span class="brand-square"></span>Harbor 7340</a>
  <nav class="main-nav">
    <a href="#" style="left:380px">Programs</a>
    <a href="#" style="left:504px">Events</a>
    <a href="#" style="left:596px">Online Store</a>
    <a href="#" style="left:750px">About Us</a>
    <a href="#" style="left:874px">Contact Us</a>
  </nav>
  <a class="signup abs" href="#">Sign-up
    <svg width="14" height="16" viewBox="0 0 14 16"><circle cx="7" cy="4" r="3.5" fill="#e6bb47"/><path d="M0 16c0-5 3-7 7-7s7 2 7 7z" fill="#e6bb47"/></svg>
  </a>
</header>

<section class="hero abs" role="img" aria-label="Snow-covered mountain range with a rocky valley"></section>
<h1 class="hero-title abs center">“EMPOWING CHANGE: BY ILLUMINATING LIVES<br>UNEXPOSED TO THE GOSPEL’S LIGHT”</h1>
<p class="hero-sub abs center">Harbor 7340’s mission is to enable the word of Jesus to be experienced by people in<br>the most remote and treacherous parts of the world</p>
<a class="btn btn-gold" href="#" style="left:273px;top:500px;width:332px;height:83px">View Our Programs</a>
<a class="btn btn-dark" href="#" style="left:625px;top:500px;width:331px;height:83px">Register for Training</a>
<div class="dots abs"><span></span><span></span><span></span><span></span></div>

<h2 class="section-title abs center" style="top:722px">Harbor 7340’s Well-Rounded Staff<br>for Specialized Training</h2>
<div class="staff-item" style="left:136px"><div class="staff-badge" role="img" aria-label="Pastor icon"></div>Pastor</div>
<div class="staff-item" style="left:285px"><div class="staff-badge" role="img" aria-label="Nutritionist icon"></div>Nutritionist</div>
<div class="staff-item" style="left:436px"><div class="staff-badge" role="img" aria-label="Dietician icon"></div>Dietician</div>
<div class="staff-item" style="left:585px"><div class="staff-badge" role="img" aria-label="Professional trainer icon"></div>Professional<br>Trainer</div>
<div class="staff-item" style="left:741px"><div class="staff-badge" role="img" aria-label="Former ranger icon"></div>Former Ranger</div>
<div class="staff-item" style="left:901px;top:898px"><div class="staff-badge" role="img" aria-label="Former special ops icon"></div>Former<br>Special Ops</div>
<div class="staff-item" style="left:1056px;top:898px"><div class="staff-badge" role="img" aria-label="Psychologist icon"></div>Psychologist</div>

<section class="why abs"></section>
<h2 class="gold-title abs center" style="top:1214px">Why Harbor 7340 is Breaking Barriers</h2>
<p class="why-copy abs">Geographical challenges make some communities difficult for missionaries to reach. The Harbor 7340 program is designed to remove the physical limitations that can hinder us from bringing the Gospel to places that seem physically impossible to reach. Harbor 7340 is founded on Romans 15:20. In his letter to the Romans, Paul requests funding to take the Gospel to Spain. In this letter, he writes:</p>
<p class="why-quote abs">“[20] and thus I make it my ambition to preach the gospel, not where Christ has already been named, lest I build on someone else’s foundation, [21] but it is written, “those who have never been told of him will see, and those who have never heard will understand.”</p>
<p class="why-ref abs center">Romans 15:20-21</p>
<a class="btn btn-gold" href="#" style="left:487px;top:1592px;width:225px;height:45px;color:var(--forest);font-size:18px">Join Our Mission</a>

<h2 class="section-title abs center" style="top:1760px;font-size:44px;color:#333">Harbor 7340 Missionary Training Approach</h2>
<p class="approach-sub abs center">Mind - Body - Spirit</p>

<div class="pillar" style="left:80px">
  <svg width="325" height="410" viewBox="0 0 325 410"><polygon points="100,50 225,50 324,145 324,310 260,409 65,409 1,310 1,145" fill="#f4f4f4" stroke="#e6bb47" stroke-width="2"/><polygon points="121,1 179,1 200,21 200,95 179,115 121,115 100,95 100,21" transform="translate(3,0)" fill="#f3d98c" stroke="#e6bb47" stroke-width="2"/></svg>
  <div class="pillar-name">Mind</div>
  <p class="pillar-text">Psychologically, we will prepare the mind through counseling, breathing techniques, and simulations in order to prepare for psychological challenges that come with being in the field</p>
</div>
<div class="pillar" style="left:443px">
  <svg width="325" height="410" viewBox="0 0 325 410"><polygon points="100,50 225,50 324,145 324,310 260,409 65,409 1,310 1,145" fill="#f4f4f4" stroke="#e6bb47" stroke-width="2"/><polygon points="121,1 179,1 200,21 200,95 179,115 121,115 100,95 100,21" transform="translate(3,3)" fill="#f3d98c" stroke="#e6bb47" stroke-width="2"/></svg>
  <div class="pillar-name" style="top:48px">Body</div>
  <p class="pillar-text">Physically, we will prepare the body to overcome any physical limitations through rigorous exercises and nutritional coaching geared specifically to the geographical area the missionary plans to go. The area the missionary plans to go.</p>
</div>
<div class="pillar" style="left:800px">
  <svg width="325" height="410" viewBox="0 0 325 410"><polygon points="100,50 225,50 324,145 324,310 260,409 65,409 1,310 1,145" fill="#f4f4f4" stroke="#e6bb47" stroke-width="2"/><polygon points="121,1 179,1 200,21 200,95 179,115 121,115 100,95 100,21" transform="translate(3,0)" fill="#f3d98c" stroke="#e6bb47" stroke-width="2"/></svg>
  <div class="pillar-name">Spirit</div>
  <p class="pillar-text" style="top:128px">Spiritually, we will prepare the soul to overcome spiritual challenges that arise in different areas of the world. Our curriculum is designed to prepare missionaries with a firm base of theological principles and destination specific training for the area in which the missionary is going</p>
</div>
<a class="btn btn-gold" href="#" style="left:375px;top:2396px;width:449px;height:68px;color:var(--forest);font-size:21px">View our detailed training program</a>

<section class="audience abs"></section>
<h2 class="gold-title abs center" style="top:2625px">Who is Harbor 7340 For?</h2>
<a class="tab" href="#" style="top:2779px">Sending Agencies for Missionaries</a>
<a class="tab active" href="#" style="top:2896px">Missionaries</a>
<a class="tab" href="#" style="top:3014px">Christian-based training program for ALL!</a>
<div class="panel abs">
  <h3>Missionaries</h3>
  <hr>
  <p>Are you independently seeking to develop your knowledge and skills independently? We are here to help! We can customize a training approach that fits your specific needs. Let us support your missionary journey to spread the Gospel to the most remote and treacherous areas in the world</p>
</div>
<a class="btn btn-gold" href="#" style="left:431px;top:3196px;width:393px;height:67px;color:var(--forest);font-size:21px">View our Training Options</a>

<section class="newsletter abs"></section>
<h2 class="news-title abs center">Join our Missionary Training: Stay up-to-date on our<br>training programs missionary success stories<br>and new program info!</h2>
<p class="news-sub abs center">Join today &amp; stay up-to-date on new product releases, shop promotions, and<br>our archery newsletters</p>
<form class="signup-form abs">
  <span class="email">Enter Your Email Address</span>
  <span class="btn subscribe">Subscribe</span>
</form>

<footer class="site-footer abs"></footer>
<a class="footer-brand abs" href="#"><span class="brand-square" style="width:28px;height:28px"></span>Harbor 7340</a>
<nav class="footer-nav abs">
  <a href="#">Programs</a><a href="#">Events</a><a href="#">Online Store</a><a href="#">About Us</a><a href="#">Contact Us</a>
</nav>
<div class="contact" style="top:3976px">
  <svg width="30" height="30" viewBox="0 0 30 30"><circle cx="15" cy="15" r="15" fill="#e6bb47"/><path d="M15 7a5 5 0 0 0-5 5c0 4 5 11 5 11s5-7 5-11a5 5 0 0 0-5-5z" fill="#2b3318"/><circle cx="15" cy="12" r="2" fill="#e6bb47"/></svg>
  <div><span class="label">LOCATION</span><br>Location Name Dummy<br>address here Pin: 123456</div>
</div>
<div class="contact" style="top:4076px;align-items:center;font-size:17px">
  <svg width="30" height="30" viewBox="0 0 30 30"><circle cx="15" cy="15" r="15" fill="#e6bb47"/><path d="M10 8l3 0 1.5 4-2 1.5a9 9 0 0 0 4 4l1.5-2 4 1.5 0 3c0 1-1 2-2 2A13 13 0 0 1 8 10c0-1 1-2 2-2z" fill="#2b3318"/></svg>
  <div><span class="label">CALL US:</span> <b>+00 555 010 742</b></div>
</div>

<div class="bottom-bar abs">
  <span class="abs" style="left:86px;top:41px">Copyright @ 2023 All rights reserved</span>
  <span class="abs" style="left:485px;top:41px">Terms of Service | Privacy Policy</span>
  <div class="socials">
    <span role="img" aria-label="Social link"></span>
    <span role="img" aria-label="Social link"></span>
    <span role="img" aria-label="Social link"></span>
    <span role="img" aria-label="Social link"></span>
  </div>
</div>

</body>
</html>
```